Business card design to suit our website

Need a nice looking business card for our business based off images from our Website and provided images. The business card will require 2 different names (for the 2 owners). The business card should include images from our website, facebook (steadfast bracket set) or the pictures provided. it should also contain all contact information.
Our website is www.steadfastbracketset.com.au
Please dont use image from top bar of website. If images are used please use the ones of our product under the buy it now tab

Target Market(s)

Automotive

Industry/Entity Type

Automotive Part

Contact Information for Business Card

Business Name. contact details including names phone number email. logo
2 business cards needed with 2 different persons names and phone number.

Colors

Designer to choose colors to be used in the design.

Requirements
Must have
• whatever looks best

```html
<!DOCTYPE html>
<html lang="en">
<head>
<meta charset="utf-8">
<title>Steadfast Bracket Works Set – Business Cards</title>
<link rel="stylesheet" href="https://fonts.googleapis.com/css2?family=Exo+2:wght@400;600;800&display=swap">
<style>
  :root{
    --page:#2a2a2a;
    --card:#161616;
    --card-light:#222;
    --red:#d0212b;
    --red-dark:#8e1018;
    --silver:#c9c9c9;
    --grey:#9a9a9a;
    --text:#e6e6e6;
  }
  *{box-sizing:border-box;margin:0;padding:0}
  html,body{width:1200px;height:1101px;overflow:hidden}
  body{background:var(--page);font-family:"Exo 2",sans-serif;color:var(--text);position:relative}
  .card{position:absolute;width:640px;height:390px;border-radius:4px;overflow:hidden;
    background:
      repeating-linear-gradient(45deg,rgba(255,255,255,.025) 0 2px,transparent 2px 4px),
      linear-gradient(160deg,var(--card-light),var(--card));
    box-shadow:0 10px 30px rgba(0,0,0,.5)}
  .card--back{left:80px;top:80px}
  .card--front{left:480px;top:630px}

  /* back */
  .back-photo{position:absolute;left:180px;top:20px;width:280px;height:210px;border-radius:50%;
    background:radial-gradient(ellipse,rgba(110,110,110,.35),rgba(40,40,40,0) 70%)}
  .tagline{position:absolute;left:60px;top:95px;width:520px;text-align:center;
    font-size:18px;letter-spacing:2.6px;line-height:1.4;color:var(--grey)}
  .back-band{position:absolute;left:0;right:0;top:270px;height:80px;background:rgba(0,0,0,.45)}
  .back-logo{position:absolute;left:200px;top:272px}
  .back-car{position:absolute;right:24px;top:278px;width:170px;height:64px;border-radius:30px 44px 8px 8px;
    background:linear-gradient(180deg,#e0333b,#7c0d14)}
  .follow{position:absolute;left:40px;top:320px;font-size:17px;color:var(--red);display:flex;align-items:center;gap:8px}
  .follow-dot{width:22px;height:22px;border-radius:50%;background:var(--red)}

  /* logo */
  .logo-name{font-weight:800;color:var(--red);line-height:1}
  .logo-sub{font-weight:800;color:var(--silver);line-height:1}
  .back-logo .logo-name{font-size:42px}
  .back-logo .logo-sub{font-size:21px;margin-top:2px}

  /* front */
  .front-car{position:absolute;right:0;top:30px;width:300px;height:150px;
    background:linear-gradient(90deg,rgba(60,60,60,0),rgba(90,90,90,.55))}
  .front-logo{position:absolute;left:40px;top:45px}
  .front-logo .logo-name{font-size:70px}
  .front-logo .logo-sub{font-size:35px;margin-top:4px}
  .rule{position:absolute;left:0;right:0;height:4px;background:linear-gradient(90deg,#777,#eee,#777)}
  .rule--top{top:185px}
  .rule--bottom{top:350px}
  .person{position:absolute;left:40px;top:198px}
  .person-name{font-size:24px;font-weight:600;color:var(--red)}
  .person-role{font-size:15px;color:var(--grey)}
  .contacts{position:absolute;left:40px;top:258px;list-style:none;font-size:19px}
  .contacts li{display:flex;align-items:center;gap:10px;height:30px}
  .contacts svg{width:20px;height:20px;flex:none}
  .product{position:absolute;right:24px;top:200px;width:170px;height:140px;border-radius:50%;
    background:radial-gradient(circle at 45% 50%,#cfcfcf,#6a6a6a 40%,rgba(30,30,30,0) 70%)}
</style>
</head>
<body>

<section class="card card--back">
  <div class="back-photo" role="img" aria-label="Faint photo of aluminium switch housings"></div>
  <p class="tagline">Remove, Rebuild, Replace your ignition switch without removing the steering column with a high quality aluminium switch housing. With a lifetime warranty.</p>
  <div class="back-band"></div>
  <div class="back-logo">
    <div class="logo-name">Steadfast</div>
    <div class="logo-sub">Bracket Works Set</div>
  </div>
  <div class="back-car" role="img" aria-label="Photo of a red sports coupe"></div>
  <div class="follow">Follow us on <span class="follow-dot"></span></div>
</section>

<section class="card card--front">
  <div class="front-car" role="img" aria-label="Faint photo of a dark sports car"></div>
  <div class="front-logo">
    <div class="logo-name">Steadfast</div>
    <div class="logo-sub">Bracket Works Set</div>
  </div>
  <div class="rule rule--top"></div>
  <div class="person">
    <div class="person-name">Dale Henley</div>
    <div class="person-role">Owner</div>
  </div>
  <ul class="contacts">
    <li><svg viewBox="0 0 20 20"><circle cx="10" cy="10" r="10" fill="var(--red)"/><path d="M6 5l2 0 1 3-1.5 1a6 6 0 003 3l1-1.5 3 1v2a1 1 0 01-1 1A9 9 0 015 6a1 1 0 011-1z" fill="#111"/></svg>1300 482 317</li>
    <li><svg viewBox="0 0 20 20"><circle cx="10" cy="10" r="10" fill="var(--red)"/><rect x="5" y="6.5" width="10" height="7" fill="#111"/><path d="M5 6.5l5 4 5-4" stroke="var(--red)" fill="none"/></svg>sales@steadfastbracketset.com.au</li>
    <li><svg viewBox="0 0 20 20"><circle cx="10" cy="10" r="10" fill="var(--red)"/><circle cx="10" cy="10" r="5.5" fill="none" stroke="#111" stroke-width="1.4"/><path d="M4.5 10h11M10 4.5c-3 3-3 8 0 11M10 4.5c3 3 3 8 0 11" stroke="#111" fill="none" stroke-width="1.2"/></svg>www.steadfastbracketset.com.au</li>
  </ul>
  <div class="rule rule--bottom"></div>
  <div class="product" role="img" aria-label="Photo of the bracket kit parts: housing, bolts and key"></div>
</section>

</body>
</html>
```